Corvane Supplies Business Card

Professional business card that stand out to our potential customers. Front and back with clean modern design

Industry/Entity Type

Oil and gas

Contact Information for Business Card

Name, address, website , office phone and cell number

Requirements
Must have
• Editable files for each employee

```html
<!DOCTYPE html>
<html lang="en">
<head>
<meta charset="utf-8">
<title>Corvane Supplies Business Card</title>
<link href="https://fonts.googleapis.com/css2?family=Montserrat:wght@400;500;700&display=swap" rel="stylesheet">
<style>
  :root {
    --backdrop: #d9d4cc;
    --card-white: #ffffff;
    --brand-red: #e8232a;
    --brand-blue: #17a8cf;
    --back-blue: #0bb0d3;
    --back-ink: #0891b2;
    --ink: #1d1d1f;
  }
  * { margin: 0; padding: 0; box-sizing: border-box; }
  html, body {
    width: 900px; height: 1200px; overflow: hidden;
    background: var(--backdrop);
    font-family: "Montserrat", sans-serif;
    color: var(--ink);
  }
  .canvas { position: relative; width: 900px; height: 1200px; }
  .card {
    position: absolute;
    border-radius: 24px;
    box-shadow: 0 6px 14px rgba(0,0,0,0.25);
  }
  .card-front { left: 80px; top: 131px; width: 742px; height: 440px; background: var(--card-white); }
  .card-back { left: 77px; top: 638px; width: 745px; height: 440px; background: var(--back-blue); }

  .brand-small {
    position: absolute; left: 35px; top: 190px;
    display: flex; align-items: center; gap: 10px;
    font-weight: 700; font-size: 20px; letter-spacing: 0.5px;
    color: var(--brand-red); text-transform: uppercase;
  }
  .brand-mark { width: 16px; height: 16px; background: var(--brand-blue); }

  .address {
    position: absolute; left: 35px; top: 236px;
    font-size: 16px; line-height: 20px;
  }
  .contacts { position: absolute; left: 35px; top: 292px; list-style: none; }
  .contacts li {
    display: flex; align-items: center; gap: 8px;
    font-size: 16px; height: 28px;
  }
  .contacts svg { width: 16px; height: 16px; fill: var(--brand-blue); }

  .person { position: absolute; right: 42px; top: 42px; width: 240px; }
  .person-name { font-weight: 700; font-size: 25px; color: var(--brand-red); line-height: 30px; }
  .person-title { font-size: 16px; line-height: 22px; }

  .brand-large {
    position: absolute; left: 480px; top: 200px; width: 230px;
    font-weight: 700; font-size: 40px; line-height: 46px;
    color: var(--brand-red); text-transform: uppercase; text-align: center;
  }

  .brand-back {
    position: absolute; left: 0; right: 0; top: 190px;
    text-align: center;
    font-weight: 700; font-size: 44px; letter-spacing: 2px;
    color: var(--back-ink); text-transform: uppercase;
  }
</style>
</head>
<body>
<main class="canvas">
  <section class="card card-front">
    <div class="brand-small"><span class="brand-mark"></span>Corvane Supplies</div>

    <p class="address">42 Summit Ridge Plaza<br>Lindale, NJ 07811 USA</p>

    <ul class="contacts">
      <li>
        <svg viewBox="0 0 16 16" aria-hidden="true"><path d="M2 6c0-2 2-3 6-3s6 1 6 3v1h-3V5.5H5V7H2z M4 8h8l1 6H3z M8 9.5a1.8 1.8 0 1 0 0 3.6a1.8 1.8 0 1 0 0-3.6z"/></svg>
        +1.555.310.0420 x123
      </li>
      <li>
        <svg viewBox="0 0 16 16" aria-hidden="true"><path d="M3 1.5l2.5-.5 1.5 3.5-1.8 1.2c.8 1.8 2.3 3.3 4.1 4.1l1.2-1.8 3.5 1.5-.5 2.5c-.3 1-1.2 1.5-2.2 1.3C6.5 12 4 9.5 2.2 4.7 2 3.7 2.2 2 3 1.5z"/></svg>
        +1.555.276.418
      </li>
      <li>
        <svg viewBox="0 0 16 16" aria-hidden="true"><path d="M1 4h14v1L8 9 1 5z M1 6.5l7 4 7-4V12H1z"/></svg>
        info@corvanesupplies.com
      </li>
      <li>
        <svg viewBox="0 0 16 16" aria-hidden="true"><circle cx="8" cy="8" r="6.5"/></svg>
        www.corvanesupplies.com
      </li>
    </ul>

    <div class="person">
      <p class="person-name">Rami Halvorsen</p>
      <p class="person-title">President</p>
    </div>

    <div class="brand-large">Corvane Supplies</div>
  </section>

  <section class="card card-back">
    <div class="brand-back">Corvane Supplies</div>
  </section>
</main>
</body>
</html>
```